2 Ridgeway Bills Motor Care Banners

Looking to have two pull up banners designed - each 33.5 x 80

First banner- Scheduled Maintenance, Diagnostics, Inspections
Voted Finest of Carrow 3 years in a row!

Second banner- Brakes, Tires, General Auto Service
Include the 3 FOC logos
2019, 2018, 2017

```html
<!DOCTYPE html>
<html lang="en">
<head>
<meta charset="utf-8">
<title>Ridgeway Bills Motor Care – Pull-Up Banners, 3 Colour Options</title>
<link rel="stylesheet" href="https://fonts.googleapis.com/css2?family=Archivo+Black&family=Arimo:wght@400;700&family=Oswald:wght@500&display=swap">
<style>
  :root {
    --navy: #2b3a67;
    --navy-deep: #22305a;
    --olive: #c9bf4e;
    --olive-text: #b3a93a;
    --red: #c4161c;
    --white: #ffffff;
    --ink: #222222;
    --sheet: #e8e8e8;
    --black: #000000;
  }
  * { box-sizing: border-box; margin: 0; padding: 0; }
  html, body { width: 1200px; height: 3000px; overflow: hidden; }
  body { position: relative; background: var(--sheet); font-family: "Arimo", Arial, sans-serif; }

  .sheet-title {
    position: absolute; left: 0; top: 0; width: 1200px; height: 93px;
    background: var(--black); color: var(--white);
    font-family: "Archivo Black", sans-serif; font-size: 34px; letter-spacing: 1px;
    display: flex; align-items: center; justify-content: center;
  }
  .option-row { position: absolute; left: 0; width: 1200px; background: linear-gradient(#f1f1f1, #dcdcdc); }
  .row-1 { top: 93px; height: 911px; }
  .row-2 { top: 1058px; height: 967px; }
  .row-3 { top: 2080px; height: 868px; }

  .label-band {
    position: absolute; left: 0; width: 1200px; height: 54px;
    font-family: "Archivo Black", sans-serif; font-size: 33px;
  }
  .label-band span { position: absolute; top: 8px; }
  .label-band span:first-child { left: 303px; }
  .label-band span:last-child { left: 748px; }
  .label-1 { top: 1004px; background: var(--navy); color: var(--white); }
  .label-2 { top: 2025px; height: 55px; background: var(--olive); color: var(--ink); }
  .label-3 { top: 2948px; height: 52px; background: var(--red); color: var(--white); }

  /* ---------- banner shell ---------- */
  .banner {
    position: absolute; width: 286px; height: 680px;
    display: grid; overflow: hidden; background: var(--white);
    box-shadow: 14px 10px 24px rgba(0,0,0,.25);
  }
  .banner-one { grid-template-rows: 85px 169px 61px 26px 41px 75px 156px 47px 20px; }
  .banner-two { grid-template-rows: 260px 64px 37px 73px 163px 52px 31px; }

  .photo-shop { background: linear-gradient(180deg, #b7c6d6 0%, #b9908a 40%, #8d8479 70%, #4a4b50 100%); }
  .photo-strip { background: linear-gradient(90deg, #5d7284 0%, #a8998a 50%, #4f5d76 100%); }

  .sign-area { display: grid; grid-template-rows: 150px 110px; }
  .photo-sign { background: linear-gradient(180deg, #a8c3e0 0%, #c8c9cf 55%, #9a8f8c 100%); }
  .sign-headline {
    background: var(--white); color: var(--navy-deep);
    font-family: "Archivo Black", sans-serif; text-align: center;
    display: flex; flex-direction: column; justify-content: center; line-height: .92;
  }
  .sign-headline .big { font-size: 40px; letter-spacing: 1px; }
  .sign-headline .small { font-size: 20px; margin-top: 4px; }

  .logo-block { display: flex; align-items: center; justify-content: center; }
  .logo-name {
    font-family: "Oswald", sans-serif; font-weight: 500; font-size: 21px;
    line-height: 1.05; text-align: center;
  }
  .banner-one .logo-block { background: var(--white); }
  .banner-one .logo-name { color: var(--olive-text); }

  .voted-band { display: flex; flex-direction: column; align-items: center; justify-content: center; background: var(--voted-bg); }
  .voted-head { font-weight: 700; font-size: 24px; line-height: 1; color: var(--voted-head); }
  .voted-sub { font-weight: 700; font-size: 14px; margin-top: 3px; color: var(--voted-sub); }

  .star-strip {
    background: var(--white); color: var(--olive);
    display: flex; justify-content: space-evenly; align-items: center; font-size: 15px; padding: 0 30px;
  }
  .message-band {
    background: var(--msg-bg); color: var(--msg-fg);
    font-size: 7.4px; line-height: 1.3; text-align: center;
    display: flex; align-items: center; justify-content: center; padding: 0 18px;
  }

  .service-list { background: var(--svc-bg); color: var(--svc-fg); list-style: none; }
  .banner-one .service-list { display: flex; flex-direction: column; justify-content: center; gap: 19px; padding-left: 28px; }
  .service-list li { display: flex; align-items: center; gap: 8px; font-size: 15.5px; }
  .banner-one .service-list li:nth-child(2), .banner-one .service-list li:nth-child(3) { padding-left: 46px; }
  .service-icon { width: 26px; height: 26px; flex: none; }

  .phone-band {
    background: var(--phone-bg); color: var(--white);
    font-weight: 700; font-size: 29px; display: flex; align-items: center; justify-content: center;
  }
  .site-strip {
    background: var(--url-bg); color: var(--url-fg);
    font-size: 8.5px; letter-spacing: 2px; display: flex; align-items: center; justify-content: center;
  }

  .banner-two .logo-block { background: var(--logo2-bg); }
  .banner-two .logo-name { color: var(--logo2-fg); }
  .banner-two .star-strip { font-size: 17px; }
  .service-panel {
    background: var(--svc-bg); color: var(--svc-fg);
    display: flex; justify-content: space-between; align-items: center; padding: 0 30px 0 20px;
  }
  .banner-two .service-list { background: none; display: flex; flex-direction: column; gap: 12px; }
  .banner-two .service-list li { font-size: 14.5px; line-height: 1.15; }
  .award-stack { display: flex; flex-direction: column; gap: 10px; }
  .award { display: block; width: 66px; height: 30px; }
  .banner-two .phone-band { background: var(--phone2-bg); font-size: 28px; }
  .banner-two .site-strip { background: var(--url2-bg); color: var(--url2-fg); }

  /* ---------- colour options ---------- */
  .theme-navy {
    --voted-bg: var(--navy); --voted-head: var(--olive); --voted-sub: var(--white);
    --msg-bg: var(--olive); --msg-fg: var(--navy-deep);
    --svc-bg: #f4f4f4; --svc-fg: var(--ink);
    --phone-bg: var(--navy); --url-bg: var(--olive); --url-fg: var(--navy-deep);
    --logo2-bg: var(--navy); --logo2-fg: var(--olive);
    --phone2-bg: var(--olive); --url2-bg: var(--navy); --url2-fg: var(--white);
  }
  .theme-olive {
    --voted-bg: var(--olive); --voted-head: var(--navy-deep); --voted-sub: var(--navy-deep);
    --msg-bg: var(--navy); --msg-fg: var(--white);
    --svc-bg: var(--navy); --svc-fg: var(--white);
    --phone-bg: var(--olive); --url-bg: var(--white); --url-fg: var(--navy-deep);
    --logo2-bg: var(--olive); --logo2-fg: var(--white);
    --phone2-bg: var(--olive); --url2-bg: var(--white); --url2-fg: var(--navy-deep);
  }
  .theme-red {
    --voted-bg: var(--red); --voted-head: var(--white); --voted-sub: var(--white);
    --msg-bg: var(--navy); --msg-fg: var(--white);
    --svc-bg: var(--navy); --svc-fg: var(--white);
    --phone-bg: var(--red); --url-bg: var(--white); --url-fg: var(--navy-deep);
    --logo2-bg: var(--red); --logo2-fg: var(--olive);
    --phone2-bg: var(--red); --url2-bg: var(--white); --url2-fg: var(--navy-deep);
  }
</style>
</head>
<body>

<svg width="0" height="0" style="position:absolute" aria-hidden="true">
  <defs>
    <symbol id="icon-service" viewBox="0 0 26 26">
      <circle cx="13" cy="13" r="11" fill="none" stroke="#c9bf4e" stroke-width="2.4" stroke-dasharray="3 2"/>
      <circle cx="13" cy="13" r="6" fill="none" stroke="currentColor" stroke-width="1.6"/>
      <path d="M10 13h6M13 10v6" stroke="currentColor" stroke-width="1.6"/>
    </symbol>
    <symbol id="award-plain" viewBox="0 0 66 30">
      <rect x="0" y="0" width="66" height="30" rx="2" fill="#ffffff"/>
      <circle cx="14" cy="15" r="10" fill="#9fb7cf"/>
      <rect x="30" y="4" width="32" height="10" fill="#c4161c"/>
      <rect x="30" y="17" width="32" height="9" fill="#d9d9d9"/>
    </symbol>
  </defs>
</svg>

<header class="sheet-title">BANNER WITH 3 COLOR OPTIONS</header>

<section class="option-row row-1 theme-navy">
  <article class="banner banner-one" style="left:241px; top:67px;">
    <div class="logo-block"><p class="logo-name">Ridgeway Bills<br>Motor Care</p></div>
    <div class="photo-shop" role="img" aria-label="Photo of the shop building with red roof and service bays"></div>
    <div class="voted-band"><p class="voted-head">VOTED FINEST OF</p><p class="voted-sub">CARROW 3 YEARS IN A ROW!</p></div>
    <div class="star-strip">★ ★ ★ ★ ★</div>
    <p class="message-band">We look forward to building a long term relationship with you. If there is anything we can do for you, don't hesitate to contact us.</p>
    <div class="photo-strip" role="img" aria-label="Photos of a wheel being serviced, tires on a rack and an engine bay"></div>
    <ul class="service-list">
      <li><svg class="service-icon"><use href="#icon-service"/></svg>Scheduled Maintenance</li>
      <li><svg class="service-icon"><use href="#icon-service"/></svg>Diagnostics</li>
      <li><svg class="service-icon"><use href="#icon-service"/></svg>Inspections</li>
    </ul>
    <div class="phone-band">555-014-2290</div>
    <div class="site-strip">www.rbmotorcare.com</div>
  </article>

  <article class="banner banner-two" style="left:675px; top:67px;">
    <div class="sign-area">
      <div class="photo-sign" role="img" aria-label="Photo of the shop front and service bays"></div>
      <p class="sign-headline"><span class="big">RIDGEWAY<br>BILLS</span><span class="small">MOTOR CARE</span></p>
    </div>
    <div class="logo-block"><p class="logo-name">Ridgeway Bills Motor Care</p></div>
    <div class="star-strip">★ ★ ★ ★ ★</div>
    <div class="photo-strip" role="img" aria-label="Photos of a wheel being serviced, tires on a rack and an engine bay"></div>
    <div class="service-panel">
      <ul class="service-list">
        <li><svg class="service-icon"><use href="#icon-service"/></svg>Brakes</li>
        <li><svg class="service-icon"><use href="#icon-service"/></svg>Tires</li>
        <li><svg class="service-icon"><use href="#icon-service"/></svg>General Auto<br>Service</li>
      </ul>
      <div class="award-stack">
        <svg class="award" role="img" aria-label="FOC award 2017"><use href="#award-plain"/></svg>
        <svg class="award" role="img" aria-label="FOC award 2019"><use href="#award-plain"/></svg>
        <svg class="award" role="img" aria-label="FOC award 2018"><use href="#award-plain"/></svg>
      </div>
    </div>
    <div class="phone-band">555-014-2290</div>
    <div class="site-strip">www.rbmotorcare.com</div>
  </article>
</section>
<div class="label-band label-1"><span>BANNER 1</span><span>BANNER 2</span></div>

<section class="option-row row-2 theme-olive">
  <article class="banner banner-one" style="left:233px; top:103px;">
    <div class="logo-block"><p class="logo-name">Ridgeway Bills<br>Motor Care</p></div>
    <div class="photo-shop" role="img" aria-label="Photo of the shop building with red roof and service bays"></div>
    <div class="voted-band"><p class="voted-head">VOTED FINEST OF</p><p class="voted-sub">CARROW 3 YEARS IN A ROW!</p></div>
    <div class="star-strip">★ ★ ★ ★ ★</div>
    <p class="message-band">We look forward to building a long term relationship with you. If there is anything we can do for you, don't hesitate to contact us.</p>
    <div class="photo-strip" role="img" aria-label="Photos of a wheel being serviced, tires on a rack and an engine bay"></div>
    <ul class="service-list">
      <li><svg class="service-icon"><use href="#icon-service"/></svg>Scheduled Maintenance</li>
      <li><svg class="service-icon"><use href="#icon-service"/></svg>Diagnostics</li>
      <li><svg class="service-icon"><use href="#icon-service"/></svg>Inspections</li>
    </ul>
    <div class="phone-band">555-014-2290</div>
    <div class="site-strip">www.rbmotorcare.com</div>
  </article>

  <article class="banner banner-two" style="left:666px; top:103px;">
    <div class="sign-area">
      <div class="photo-sign" role="img" aria-label="Photo of the shop front and service bays"></div>
      <p class="sign-headline"><span class="big">RIDGEWAY<br>BILLS</span><span class="small">MOTOR CARE</span></p>
    </div>
    <div class="logo-block"><p class="logo-name">Ridgeway Bills Motor Care</p></div>
    <div class="star-strip">★ ★ ★ ★ ★</div>
    <div class="photo-strip" role="img" aria-label="Photos of a wheel being serviced, tires on a rack and an engine bay"></div>
    <div class="service-panel">
      <ul class="service-list">
        <li><svg class="service-icon"><use href="#icon-service"/></svg>Brakes</li>
        <li><svg class="service-icon"><use href="#icon-service"/></svg>Tires</li>
        <li><svg class="service-icon"><use href="#icon-service"/></svg>General Auto<br>Service</li>
      </ul>
      <div class="award-stack">
        <svg class="award" role="img" aria-label="FOC award 2017"><use href="#award-plain"/></svg>
        <svg class="award" role="img" aria-label="FOC award 2019"><use href="#award-plain"/></svg>
        <svg class="award" role="img" aria-label="FOC award 2018"><use href="#award-plain"/></svg>
      </div>
    </div>
    <div class="phone-band">555-014-2290</div>
    <div class="site-strip">www.rbmotorcare.com</div>
  </article>
</section>
<div class="label-band label-2"><span>BANNER 1</span><span>BANNER 2</span></div>

<section class="option-row row-3 theme-red">
  <article class="banner banner-one" style="left:241px; top:83px;">
    <div class="logo-block"><p class="logo-name">Ridgeway Bills<br>Motor Care</p></div>
    <div class="photo-shop" role="img" aria-label="Photo of the shop building with red roof and service bays"></div>
    <div class="voted-band"><p class="voted-head">VOTED FINEST OF</p><p class="voted-sub">CARROW 3 YEARS IN A ROW!</p></div>
    <div class="star-strip">★ ★ ★ ★ ★</div>
    <p class="message-band">We look forward to building a long term relationship with you. If there is anything we can do for you, don't hesitate to contact us.</p>
    <div class="photo-strip" role="img" aria-label="Photos of a wheel being serviced, tires on a rack and an engine bay"></div>
    <ul class="service-list">
      <li><svg class="service-icon"><use href="#icon-service"/></svg>Scheduled Maintenance</li>
      <li><svg class="service-icon"><use href="#icon-service"/></svg>Diagnostics</li>
      <li><svg class="service-icon"><use href="#icon-service"/></svg>Inspections</li>
    </ul>
    <div class="phone-band">555-014-2290</div>
    <div class="site-strip">www.rbmotorcare.com</div>
  </article>

  <article class="banner banner-two" style="left:675px; top:83px;">
    <div class="sign-area">
      <div class="photo-sign" role="img" aria-label="Photo of the shop front and service bays"></div>
      <p class="sign-headline"><span class="big">RIDGEWAY<br>BILLS</span><span class="small">MOTOR CARE</span></p>
    </div>
    <div class="logo-block"><p class="logo-name">Ridgeway Bills Motor Care</p></div>
    <div class="star-strip">★ ★ ★ ★ ★</div>
    <div class="photo-strip" role="img" aria-label="Photos of a wheel being serviced, tires on a rack and an engine bay"></div>
    <div class="service-panel">
      <ul class="service-list">
        <li><svg class="service-icon"><use href="#icon-service"/></svg>Brakes</li>
        <li><svg class="service-icon"><use href="#icon-service"/></svg>Tires</li>
        <li><svg class="service-icon"><use href="#icon-service"/></svg>General Auto<br>Service</li>
      </ul>
      <div class="award-stack">
        <svg class="award" role="img" aria-label="FOC award 2017"><use href="#award-plain"/></svg>
        <svg class="award" role="img" aria-label="FOC award 2019"><use href="#award-plain"/></svg>
        <svg class="award" role="img" aria-label="FOC award 2018"><use href="#award-plain"/></svg>
      </div>
    </div>
    <div class="phone-band">555-014-2290</div>
    <div class="site-strip">www.rbmotorcare.com</div>
  </article>
</section>
<div class="label-band label-3"><span>BANNER 1</span><span>BANNER 2</span></div>

</body>
</html>
```